Business Card for Language School (2 locations)

We need a sleek business card for a language school that is looking to update our image to be more professional. We work with students ages Pre-Kindergarten through adults. Our idea is to have an all-black business card with white or silver lettering. On the front will be the name of our school (Bright Meadow English Academy), and on the back there will be information for our location, phone number, email, and website (and possibly social media information). We have two school branches, so the address, phone number, and email address will be different for each branch, but all of the other information will stay the same. We'd like each branch to have a different color card edge that is neon. We are also open to suggestions and new ideas!

Some answers to questions we have received:
1. The reason we haven't added a logo is because we are looking to get a new one. We hadn't originally planned to do that at this time, but we are going to look into updating our project to include that as another aspect of it. We had previously planned to just include the school name on the front without a logo at this time.
2. We currently have two branches of our school, and we want our business card design to be uniform for each location. While it might make sense to put the information on one card right now, we plan to have more locations in the future, so we want to plan ahead with a unified design right now.
3. Our school addresses and phone numbers can be found on our website: www.brightmeadowlingo.example (at the bottom of the page)!
Updates

Part of this contest is also a new logo design. Our previous design was a train, which we would be open to keeping if it had an updated, sleeker design.

Contact Information for Business Card

Card #1:
Bright Meadow English Academy (Qinglu Branch)
Fuxing W. Rd. Sec. 3, Lane 412, No. 58, 1F
Beitou District, Taipei City 11260
02-2941-3086
qinglu@brightmeadowlingo.example

Card #2:
Bright Meadow English Academy (Heping Branch)
Linsen Road, No. 318, 1F
Songshan District, Taipei City 10587
02-2764-1520
heping@brightmeadowlingo.example

Both cards:
Website: www.brightmeadowlingo.example
Facebook: www.facebook.com/brightmeadowlingo
Instagram: @brightmeadowlingo

```html
<!DOCTYPE html>
<html lang="en">
<head>
<meta charset="utf-8">
<title>Bright Meadow English Academy – Business Card</title>
<link rel="stylesheet" href="https://fonts.googleapis.com/css2?family=Overpass:wght@600;700;800&display=swap">
<style>
  :root {
    --page: #ffffff;
    --card: #000000;
    --ink: #ffffff;
    --neon: #ffa300;
    --neon-glow: rgba(255, 163, 0, 0.75);
  }
  html, body {
    margin: 0;
    padding: 0;
    width: 1200px;
    height: 1200px;
    overflow: hidden;
    background: var(--page);
    font-family: "Overpass", "Helvetica Neue", Arial, sans-serif;
    color: var(--ink);
  }
  .canvas { position: relative; width: 1200px; height: 1200px; }
  .card {
    position: absolute;
    left: 212px;
    width: 776px;
    height: 475px;
    background: var(--card);
  }
  .card--front { top: 87px; }
  .card--back { top: 639px; }

  .neon-bar {
    position: absolute;
    background: var(--neon);
    box-shadow: 0 0 8px 2px var(--neon-glow);
  }
  .neon-bar--upper { left: 153px; top: 0; width: 18px; height: 191px; }
  .neon-bar--lower { left: 153px; top: 418px; width: 18px; height: 57px; }
  .neon-bar--band { left: 0; top: 402px; width: 776px; height: 10px; }

  .brand-mark {
    position: absolute;
    left: 38px;
    top: 70px;
    width: 100px;
    font-weight: 700;
    font-size: 17px;
    line-height: 1.1;
    text-align: center;
  }

  .school-name {
    position: absolute;
    left: 228px;
    top: 38px;
    margin: 0;
    font-weight: 700;
    font-size: 31px;
    line-height: 1.2;
  }
  .branch-name {
    position: absolute;
    left: 228px;
    top: 80px;
    margin: 0;
    font-weight: 700;
    font-size: 20px;
  }

  .contact-list { list-style: none; margin: 0; padding: 0; }
  .contact-item {
    position: absolute;
    left: 148px;
    display: flex;
    align-items: center;
    font-weight: 700;
    font-size: 13px;
    letter-spacing: 0.4px;
    line-height: 1.3;
  }
  .contact-item--address { top: 214px; }
  .contact-item--phone { top: 265px; }
  .contact-item--email { top: 316px; }
  .contact-item--web { top: 366px; }
  .contact-icon {
    width: 27px;
    height: 27px;
    flex: none;
    margin-right: 53px;
  }

  .back-brand {
    position: absolute;
    left: 0;
    top: 210px;
    width: 776px;
    display: flex;
    justify-content: center;
    align-items: center;
    font-weight: 700;
    font-size: 26px;
    line-height: 1;
  }
  .back-brand__dot {
    width: 30px;
    height: 30px;
    margin-right: 14px;
    border-radius: 50%;
    background: var(--ink);
    flex: none;
  }

  .social {
    position: absolute;
    top: 431px;
    display: flex;
    align-items: center;
    font-weight: 700;
    font-size: 13.5px;
    letter-spacing: 0.4px;
  }
  .social--facebook { left: 178px; }
  .social--instagram { left: 416px; }
  .social__dot {
    width: 27px;
    height: 27px;
    border-radius: 50%;
    background: var(--neon);
    margin-right: 35px;
  }
</style>
</head>
<body>
<main class="canvas">

  <section class="card card--front" aria-label="Business card front">
    <div class="neon-bar neon-bar--upper"></div>
    <div class="neon-bar neon-bar--lower"></div>

    <div class="brand-mark">Bright<br>Meadow</div>

    <h1 class="school-name">Bright Meadow English Academy</h1>
    <h2 class="branch-name">Heping Branch</h2>

    <ul class="contact-list">
      <li class="contact-item contact-item--address">
        <svg class="contact-icon" viewBox="0 0 28 28" aria-hidden="true">
          <circle cx="14" cy="14" r="14" fill="var(--neon)"/>
          <path d="M14 6.5a5 5 0 0 0-5 5c0 3.8 5 9.5 5 9.5s5-5.7 5-9.5a5 5 0 0 0-5-5z" fill="#fff"/>
          <circle cx="14" cy="11.5" r="2" fill="var(--neon)"/>
        </svg>
        <span>Linsen Road, No. 318, 1F<br>Songshan District, Taipei City 10587</span>
      </li>
      <li class="contact-item contact-item--phone">
        <svg class="contact-icon" viewBox="0 0 28 28" aria-hidden="true">
          <circle cx="14" cy="14" r="14" fill="var(--neon)"/>
          <path d="M9 7.5l2.5-.5 1.5 3.5-1.7 1.3a8 8 0 0 0 4 4l1.3-1.7 3.5 1.5-.5 2.5c-.3 1-1.4 1.6-2.4 1.3A12 12 0 0 1 7.7 9.9c-.3-1 .3-2.1 1.3-2.4z" fill="#fff"/>
          <path d="M15.5 8a4.5 4.5 0 0 1 4.5 4.5M15.5 5.5a7 7 0 0 1 7 7" stroke="#fff" stroke-width="1.3" fill="none" stroke-linecap="round"/>
        </svg>
        <span>02-2764-1520</span>
      </li>
      <li class="contact-item contact-item--email">
        <svg class="contact-icon" viewBox="0 0 28 28" aria-hidden="true">
          <circle cx="14" cy="14" r="14" fill="var(--neon)"/>
          <rect x="7" y="9" width="14" height="10" rx="1" fill="#fff"/>
          <path d="M7.5 9.5l6.5 5 6.5-5M7.5 18.5l4.5-4M20.5 18.5l-4.5-4" stroke="var(--neon)" stroke-width="1.1" fill="none"/>
        </svg>
        <span>heping@brightmeadowlingo.example</span>
      </li>
      <li class="contact-item contact-item--web">
        <svg class="contact-icon" viewBox="0 0 28 28" aria-hidden="true">
          <circle cx="14" cy="14" r="14" fill="var(--neon)"/>
          <g stroke="#fff" stroke-width="1.2" fill="none">
            <circle cx="14" cy="14" r="7"/>
            <ellipse cx="14" cy="14" rx="3" ry="7"/>
            <path d="M7 14h14M8 10.5h12M8 17.5h12"/>
          </g>
        </svg>
        <span>www.brightmeadowlingo.example</span>
      </li>
    </ul>
  </section>

  <section class="card card--back" aria-label="Business card back">
    <div class="back-brand">
      <span class="back-brand__dot" aria-hidden="true"></span>
      <span class="back-brand__name">Bright Meadow English Academy</span>
    </div>

    <div class="neon-bar neon-bar--band"></div>

    <div class="social social--facebook">
      <span class="social__dot" aria-hidden="true"></span>
      <span>brightmeadowlingo</span>
    </div>
    <div class="social social--instagram">
      <span class="social__dot" aria-hidden="true"></span>
      <span>@brightmeadowlingo</span>
    </div>
  </section>

</main>
</body>
</html>
```